Closed loop end of life cycle for electronics Loop.

Sustainability Closed Loop. I need six sections on the Closed Loop
1-End-of-life Product & Mfg. Scrap
2-UBNE Services
3-Mechanical Processing
4-Precious Metals Refining
5-Metal Products Manufactured
6-Products return to OEMs
Target Market(s)
Vorex, Norby, KGWR, other major manufacturers of electronics and semiconductor
Industry/Entity Type
Sustainablek
Font styles to use
Serif
Sans Serif
Colors
0054AA
0677BA
7BADD7
CADEEF
E8F1F8
0094D4
00A9DD
6FCCEA
C7EBF8
E9F6FB
00AB8E
00BBA5
67D7C9
C6EFE9
E9F9F6
Requirements
Must have
- Sustainability Closed Loop. I need six sections on the Closed Loop ring below.

```html
<!DOCTYPE html>
<html lang="en">
<head>
<meta charset="utf-8">
<title>Sustainability Closed Loop</title>
<link rel="stylesheet" href="https://fonts.googleapis.com/css2?family=Roboto+Condensed:wght@700&display=swap">
<style>
  :root {
    --paper: #ffffff;
    --trace: #addeee;
    --trace-soft: #e4f4fa;
    --petal-collect: #00aeef;
    --petal-services: #8dc63f;
    --petal-mechanical: #f7941d;
    --petal-refining: #ef4136;
    --petal-manufacture: #662d91;
    --petal-return: #2db573;
    --label: #ffffff;
  }
  html, body {
    margin: 0;
    padding: 0;
    width: 1200px;
    height: 1200px;
    overflow: hidden;
    background: var(--paper);
  }
  .loop-canvas {
    display: block;
    width: 1200px;
    height: 1200px;
  }
  .trace-stop-inner { stop-color: var(--trace); stop-opacity: 0.55; }
  .trace-stop-mid { stop-color: var(--trace-soft); stop-opacity: 0.9; }
  .trace-stop-outer { stop-color: var(--paper); stop-opacity: 1; }
  .petal { stroke: var(--paper); stroke-width: 9; stroke-linejoin: round; }
  .petal--collect { fill: var(--petal-collect); }
  .petal--services { fill: var(--petal-services); }
  .petal--mechanical { fill: var(--petal-mechanical); }
  .petal--refining { fill: var(--petal-refining); }
  .petal--manufacture { fill: var(--petal-manufacture); }
  .petal--return { fill: var(--petal-return); }
  .step-badge { fill: var(--paper); }
  .step-number {
    font-family: "Roboto Condensed", "Arial Narrow", sans-serif;
    font-weight: 700;
    font-size: 104px;
    text-anchor: middle;
    dominant-baseline: central;
  }
  .step-label {
    font-family: "Roboto Condensed", "Arial Narrow", sans-serif;
    font-weight: 700;
    font-size: 35px;
    fill: var(--label);
    text-anchor: middle;
    dominant-baseline: central;
  }
  .num-collect { fill: var(--petal-collect); }
  .num-services { fill: var(--petal-services); }
  .num-mechanical { fill: var(--petal-mechanical); }
  .num-refining { fill: var(--petal-refining); }
  .num-manufacture { fill: var(--petal-manufacture); }
  .num-return { fill: var(--petal-return); }
</style>
</head>
<body>
<svg class="loop-canvas" viewBox="0 0 1500 1500" aria-label="Sustainability closed loop in six steps">
  <defs>
    <radialGradient id="trace-field-fill" cx="50%" cy="50%" r="50%">
      <stop offset="0%" class="trace-stop-inner"/>
      <stop offset="65%" class="trace-stop-mid"/>
      <stop offset="100%" class="trace-stop-outer"/>
    </radialGradient>
    <path id="petal-shape" d="M742,725 C690,660 600,590 480,577 C455,500 460,400 505,322 C640,350 760,420 780,520 C795,600 770,680 742,725 Z"/>
  </defs>

  <rect class="circuit-field" x="30" y="80" width="1440" height="1350" fill="url(#trace-field-fill)"
        role="img" aria-label="Light blue circuit board traces radiating outward from the loop"/>

  <g class="loop-petals">
    <use href="#petal-shape" class="petal petal--collect"/>
    <use href="#petal-shape" class="petal petal--services" transform="rotate(60 750 750)"/>
    <use href="#petal-shape" class="petal petal--mechanical" transform="rotate(120 750 750)"/>
    <use href="#petal-shape" class="petal petal--refining" transform="rotate(180 750 750)"/>
    <use href="#petal-shape" class="petal petal--manufacture" transform="rotate(240 750 750)"/>
    <use href="#petal-shape" class="petal petal--return" transform="rotate(300 750 750)"/>
  </g>

  <g class="step-badges">
    <circle class="step-badge" cx="564" cy="425" r="66"/>
    <text class="step-number num-collect" x="564" y="425">1</text>
    <circle class="step-badge" cx="938" cy="428" r="66"/>
    <text class="step-number num-services" x="938" y="428">2</text>
    <circle class="step-badge" cx="1125" cy="750" r="66"/>
    <text class="step-number num-mechanical" x="1125" y="750">3</text>
    <circle class="step-badge" cx="938" cy="1073" r="66"/>
    <text class="step-number num-refining" x="938" y="1073">4</text>
    <circle class="step-badge" cx="564" cy="1073" r="66"/>
    <text class="step-number num-manufacture" x="564" y="1073">5</text>
    <circle class="step-badge" cx="377" cy="750" r="66"/>
    <text class="step-number num-return" x="377" y="750">6</text>
  </g>

  <g class="step-labels">
    <text class="step-label" x="668" y="518">End-of-life</text>
    <text class="step-label" x="668" y="561">Product &amp; Mfg.</text>
    <text class="step-label" x="672" y="604">Scrap</text>

    <text class="step-label" x="898" y="573">UBNE</text>
    <text class="step-label" x="900" y="617">Services</text>

    <text class="step-label" x="933" y="762">Mechanical</text>
    <text class="step-label" x="937" y="805">Processing</text>

    <text class="step-label" x="853" y="948">Precious Metals</text>
    <text class="step-label" x="857" y="991">Refining</text>

    <text class="step-label" x="585" y="878">Metal</text>
    <text class="step-label" x="585" y="921">Products</text>
    <text class="step-label" x="588" y="965">Manufactured</text>

    <text class="step-label" x="551" y="693">Products return</text>
    <text class="step-label" x="555" y="736">to OEMs</text>
  </g>
</svg>
</body>
</html>
```